New ecommerce website needed for Epoxy Retailer

We need a new shopify website designed and built for our epoxy supply store.
We sell Epoxy, wood, epoxy furniture, supplies and provide classes on how to use epoxy.
We are looking for a website with a home page and 7 primary navigation links at the top. Some of these links should have a drop down menu with the below listed pages linked to them...
Sub Pages:
- Glacier Resin
- Epoxy
- Pigments
- Heron Balm
- Molds
- Silicone
- HDPE
- Wood
- Live Edge
- Ovals & Rounds
- Pre-cut
- Charcuterie Wood
- Custom Milling
- Wholesale
- Supplies
- Furniture
-Education
- In person workshops
- My courses (are we able to have a login section for customers to see their purchases?)
- About Us

```html
<!DOCTYPE html>
<html lang="en">
<head>
<meta charset="utf-8">
<title>Timberpour Studio – Epoxy Supply Store</title>
<link rel="stylesheet" href="https://fonts.googleapis.com/css2?family=Bebas+Neue&family=Arimo:wght@400;700&display=swap">
<style>
:root{
  --ink:#111111;
  --text:#333333;
  --muted:#8a8a8a;
  --band:#efefef;
  --footer:#231f20;
  --footer-text:#d8d8d8;
  --star:#e8a020;
  --white:#ffffff;
  --btn:#e6e6e6;
}
*{margin:0;padding:0;box-sizing:border-box}
html,body{width:1200px;height:3975px;overflow:hidden;background:var(--white)}
body{position:relative;font-family:"Arimo",Arial,sans-serif;color:var(--text)}
.abs{position:absolute}
.display{font-family:"Bebas Neue",Impact,sans-serif;color:var(--ink);letter-spacing:.5px}

/* header */
.site-header{left:0;top:0;width:1200px;height:85px;background:var(--white);z-index:3}
.brand{left:65px;top:0;width:144px;height:144px;border-radius:50%;background:var(--white);z-index:4;display:flex;align-items:center;justify-content:center}
.brand-name{font-family:"Bebas Neue",Impact,sans-serif;font-size:26px;line-height:1;color:var(--ink);text-align:center}
.main-nav{left:504px;top:30px;display:flex;gap:20px;align-items:center;font-family:"Bebas Neue",sans-serif;font-size:17px;color:var(--ink)}
.header-icons{left:986px;top:29px;display:flex;gap:18px}

/* hero */
.hero{left:0;top:85px;width:1200px;height:655px;background:linear-gradient(120deg,#3b3b3b 0%,#6a5a45 35%,#274a7a 55%,#5a4a38 75%,#2b2b2b 100%)}
.hero-shade{left:0;top:85px;width:1200px;height:655px;background:linear-gradient(90deg,rgba(0,0,0,.45),rgba(0,0,0,0) 60%)}
.hero-kicker{left:88px;top:304px;font-size:21px;font-weight:700;color:var(--white);letter-spacing:.5px}
.hero-title{left:88px;top:338px;font-size:70px;line-height:72px;color:var(--white)}
.btn-light{left:88px;top:497px;width:126px;height:44px;background:var(--white);color:var(--ink);font-size:16px;font-weight:700;display:flex;align-items:center;justify-content:center;letter-spacing:.5px}
.dots{display:flex;gap:8px}
.dot{width:13px;height:13px;border-radius:50%;background:#c9c9c9}
.dot.on{background:var(--white)}

/* sections */
.kicker{font-size:12px;font-weight:700;color:var(--ink);letter-spacing:.5px}
.section-title{font-size:38px;line-height:1;text-align:center;width:1200px;left:0}
.para{font-size:15.5px;line-height:25px;color:var(--text)}
.photo{background:linear-gradient(135deg,#2c2c2c,#6b4a30 55%,#d9d4cc)}
.drop{box-shadow:0 40px 40px -25px rgba(0,0,0,.35)}
.btn-grey{background:var(--btn);color:var(--ink);font-size:13px;font-weight:700;display:flex;align-items:center;justify-content:center;letter-spacing:.4px}

.band{left:0;top:1758px;width:1200px;height:586px;background:var(--band)}
.product-card{top:1479px;height:342px;background:var(--white);box-shadow:0 2px 10px rgba(0,0,0,.05);text-align:center}
.product-img{position:absolute;left:50%;top:48px;transform:translateX(-50%);border-radius:4px}
.stars{color:var(--star);font-size:15px;letter-spacing:1px}
.product-name{font-size:18px;color:var(--ink)}
.price{font-size:21px;font-weight:700;color:var(--muted)}
.card-meta{position:absolute;left:0;right:0;top:232px}

.video{left:575px;top:1960px;width:475px;height:473px;background:linear-gradient(160deg,#dfe5ea 0%,#9aa6b0 35%,#6b4632 60%,#3c4450 100%)}
.play{left:768px;top:2151px;width:90px;height:90px;border-radius:50%;background:rgba(255,255,255,.3);display:flex;align-items:center;justify-content:center}

.blog-img{top:2589px;width:320px;height:241px}
.blog-date{top:2858px;font-family:"Bebas Neue",sans-serif;font-size:14px;color:var(--muted)}
.blog-title{top:2882px;font-size:23px}
.blog-text{top:2920px;width:260px;font-size:15px;line-height:22px;color:var(--text)}

.avatar{left:532px;top:3158px;width:136px;height:136px;border-radius:50%;background:radial-gradient(circle at 50% 40%,#c9a58a,#6e8ba6 70%,#e8e8e8)}
.client-name{left:0;width:1200px;top:3310px;text-align:center;font-size:13px;font-weight:700;color:var(--ink)}
.quote{left:320px;width:560px;top:3372px;text-align:center;font-size:14.5px;line-height:25px;color:var(--text)}

/* footer */
.site-footer{left:0;top:3554px;width:1200px;height:421px;background:var(--footer)}
.footer-brand{left:110px;top:3673px;width:154px;height:154px;border-radius:50%;border:3px solid var(--white);display:flex;align-items:center;justify-content:center}
.footer-title{top:3622px;font-size:27px;color:var(--white)}
.footer-list{list-style:none;font-size:16px;line-height:25px;color:var(--footer-text)}
.contact-row{display:flex;align-items:center;gap:10px;font-size:16px;color:var(--footer-text);height:26px}
.social{display:flex;gap:6px}
.social span{width:30px;height:30px;background:var(--white);display:block}
.newsletter-input{left:864px;top:3772px;width:242px;height:30px;border:1px solid var(--white);background:var(--white);display:flex}
.newsletter-input .field{flex:1;font-size:15px;color:#777;padding:5px 6px}
.newsletter-input .go{width:76px;margin:3px;background:var(--footer);color:var(--white);font-size:11px;font-weight:700;display:flex;align-items:center;justify-content:center}
.footer-rule{left:88px;top:3922px;width:1022px;height:1px;background:#6b6b6b}
.copyright{left:0;width:1200px;top:3937px;text-align:center;font-size:15px;color:var(--footer-text)}
</style>
</head>
<body>

<header class="abs site-header">
  <nav class="abs main-nav">
    <svg width="16" height="15" viewBox="0 0 16 15" aria-label="Home"><path d="M8 1 1 7h2v7h4V10h2v4h4V7h2z" fill="#777"/></svg>
    <span>Products</span><span>Wholesale</span><span>Supplies</span><span>Workshops</span><span>About Us</span><span>Contact</span>
  </nav>
  <div class="abs header-icons">
    <svg width="20" height="20" viewBox="0 0 20 20" aria-label="Search"><circle cx="8" cy="8" r="6" fill="none" stroke="#111" stroke-width="2"/><path d="M12.5 12.5 18 18" stroke="#111" stroke-width="2"/></svg>
    <svg width="20" height="20" viewBox="0 0 20 20" aria-label="Account"><circle cx="10" cy="6" r="4" fill="none" stroke="#111" stroke-width="2"/><path d="M2 19c1-5 15-5 16 0" fill="none" stroke="#111" stroke-width="2"/></svg>
    <svg width="20" height="20" viewBox="0 0 20 20" aria-label="Wishlist"><path d="M10 18 2.5 10.5A4.5 4.5 0 0 1 10 4a4.5 4.5 0 0 1 7.5 6.5z" fill="none" stroke="#111" stroke-width="2"/></svg>
    <svg width="18" height="20" viewBox="0 0 18 20" aria-label="Cart"><rect x="2" y="5" width="14" height="14" fill="none" stroke="#111" stroke-width="2"/><path d="M6 5V3a3 3 0 0 1 6 0v2" fill="none" stroke="#111" stroke-width="2"/></svg>
  </div>
</header>
<div class="abs brand"><span class="brand-name">Timberpour<br>Studio</span></div>

<section>
  <div class="abs hero" role="img" aria-label="Live-edge wood table with blue epoxy river on a black patterned metal base"></div>
  <div class="abs hero-shade"></div>
  <p class="abs hero-kicker">DOCORATE YOUR HOME</p>
  <h1 class="abs display hero-title" style="color:var(--white)">Built for our epoxy<br>supply store</h1>
  <a class="abs btn-light">BUY NOW</a>
  <div class="abs dots" style="left:571px;top:700px"><span class="dot"></span><span class="dot on"></span><span class="dot"></span></div>
</section>

<section>
  <div class="abs photo drop" style="left:173px;top:834px;width:475px;height:475px" role="img" aria-label="Dining room with walnut and white epoxy table and sideboard"></div>
  <p class="abs kicker" style="left:726px;top:931px">ABOUT US</p>
  <h2 class="abs display" style="left:726px;top:954px;font-size:36px">We sell epoxy, wood,</h2>
  <p class="abs para" style="left:726px;top:1005px;width:340px">Lorem ipsum dolor sit amet, consectetur adipiscing elit, sed do eiusmod tempor incididunt ut labore et dolore magna aliqua. Quis ipsum suspendisse ultrices gravida. Risus commodo viverra maecenas accumsan lacus vel facilisis.</p>
  <a class="abs btn-grey" style="left:726px;top:1177px;width:118px;height:43px">READ MORE</a>
</section>

<div class="abs band"></div>
<section>
  <h2 class="abs display section-title" style="top:1413px">Our products</h2>
  <article class="abs product-card" style="left:100px;width:239px">
    <div class="product-img" style="width:110px;height:140px;background:linear-gradient(180deg,#e8e8e8,#2a7fc4 40%,#dfe9f2)" role="img" aria-label="Tin of marine epoxy coating"></div>
    <div class="card-meta"><div class="stars">★★★★★</div><div class="product-name">Glacier Resin</div><div class="price">$25.00</div></div>
  </article>
  <article class="abs product-card" style="left:356px;width:487px">
    <div class="product-img" style="width:400px;height:150px;background:linear-gradient(180deg,#7a4a2a 0%,#a06a3e 45%,#c9a964 70%,#ffffff 100%)" role="img" aria-label="Epoxy resin dining table with gold legs"></div>
    <div class="card-meta"><div class="stars">★★★★★</div><div class="product-name">Epoxy Furniture</div><div class="price">$25.00</div></div>
  </article>
  <article class="abs product-card" style="left:860px;width:239px">
    <div class="product-img" style="width:200px;height:140px;background:radial-gradient(ellipse at 50% 55%,#e8b98a,#c98a58 60%,#ffffff 80%)" role="img" aria-label="Stack of split wood blocks"></div>
    <div class="card-meta"><div class="stars">★★★★★</div><div class="product-name">Wood</div><div class="price">$25.00</div></div>
  </article>
  <div class="abs dots" style="left:567px;top:1856px"><span class="dot"></span><span class="dot"></span><span class="dot"></span></div>
</section>

<section>
  <p class="abs kicker" style="left:171px;top:2023px">WORKSHOP</p>
  <h2 class="abs display" style="left:171px;top:2044px;font-size:36px">We make epoxy furniture,</h2>
  <p class="abs para" style="left:171px;top:2096px;width:335px;font-size:14.5px">Lorem ipsum dolor sit amet, consectetur adipiscing elit, sed do eiusmod tempor incididunt ut labore et dolore magna aliqua. Quis ipsum suspendisse ultrices gravida. Risus commodo viverra maecenas accumsan lacus vel facilisis.</p>
  <div class="abs video drop" role="img" aria-label="Video still of river table and stools by a snowy window"></div>
  <div class="abs play"><svg width="20" height="22" viewBox="0 0 20 22" aria-label="Play"><path d="M3 2 18 11 3 20z" fill="#fff"/></svg></div>
</section>

<section>
  <h2 class="abs display section-title" style="top:2522px">Latest blog</h2>
  <div class="abs blog-img" style="left:109px;background:linear-gradient(135deg,#3a3a3a,#2c7fa0 50%,#8a3f7a)" role="img" aria-label="Pouring coloured resin onto a round board"></div>
  <div class="abs blog-img" style="left:439px;background:linear-gradient(135deg,#cfcfcf,#4a4a4a 50%,#2a2a2a)" role="img" aria-label="Woman working on a dark wood slab"></div>
  <div class="abs blog-img" style="left:768px;background:linear-gradient(135deg,#9aa8b0,#c8a060 55%,#7a93a8)" role="img" aria-label="Pouring clear epoxy onto wood"></div>

  <p class="abs blog-date" style="left:111px">05-01-2023</p>
  <h3 class="abs display blog-title" style="left:111px">Some heading goes here</h3>
  <p class="abs blog-text" style="left:111px;font-size:14px">Lorem ipsum dolor sit amet, consectetur adip iscing elit, sed do eiusmod tempor</p>

  <p class="abs blog-date" style="left:441px">05-01-2023</p>
  <h3 class="abs display blog-title" style="left:441px">Some heading goes here</h3>
  <p class="abs blog-text" style="left:441px">Lorem ipsum dolor sit amet, consectetur adipiscing elit, sed do eiusmod tempor</p>

  <p class="abs blog-date" style="left:770px">05-01-2023</p>
  <h3 class="abs display blog-title" style="left:770px">Some heading goes here</h3>
  <p class="abs blog-text" style="left:770px">Lorem ipsum dolor sit amet, consectetur adipiscing elit, sed do eiusmod tempor</p>
</section>

<section>
  <h2 class="abs display section-title" style="top:3077px">What our client says</h2>
  <div class="abs avatar" role="img" aria-label="Client portrait"></div>
  <p class="abs client-name">Dorian Castell</p>
  <div class="abs stars" style="left:0;width:1200px;top:3328px;text-align:center">★★★★★</div>
  <p class="abs quote">Lorem ipsum dolor sit amet, consectetur adipiscing elit, sed do eiusmod tempor incididunt ut labore et dolore magna aliqua. Quis ipsum suspendisse ultrices gravida. Risus commodo viverra maecenas accumsan lacus vel facilisis.</p>
  <div class="abs dots" style="left:571px;top:3474px"><span class="dot" style="background:#666"></span><span class="dot" style="background:#666"></span><span class="dot" style="background:#111"></span></div>
</section>

<footer>
  <div class="abs site-footer"></div>
  <div class="abs footer-brand"><span class="brand-name" style="color:var(--white)">Timberpour<br>Studio</span></div>

  <h4 class="abs display footer-title" style="left:356px">Useful links</h4>
  <ul class="abs footer-list" style="left:356px;top:3690px">
    <li>Home</li><li>Products</li><li>Wholesale</li><li>Supplies</li><li>Workshops</li><li>About us</li><li>Contact</li>
  </ul>

  <h4 class="abs display footer-title" style="left:611px">Follow us</h4>
  <div class="abs" style="left:613px;top:3688px">
    <div class="contact-row"><svg width="10" height="14" viewBox="0 0 10 14" aria-label="Address"><path d="M5 0a5 5 0 0 1 5 5c0 4-5 9-5 9S0 9 0 5a5 5 0 0 1 5-5z" fill="#fff"/><circle cx="5" cy="5" r="2" fill="#231f20"/></svg>Some goes address here</div>
    <div class="contact-row"><svg width="12" height="12" viewBox="0 0 12 12" aria-label="Phone"><path d="M2 0h3l1 3-2 1a7 7 0 0 0 4 4l1-2 3 1v3c0 1-1 2-2 2A11 11 0 0 1 0 2C0 1 1 0 2 0z" fill="#fff"/></svg>012 345 678</div>
    <div class="contact-row"><svg width="13" height="10" viewBox="0 0 13 10" aria-label="Email"><rect width="13" height="10" fill="#fff"/><path d="M0 0 6.5 6 13 0" fill="none" stroke="#231f20"/></svg>Some goes email here</div>
  </div>
  <div class="abs social" style="left:613px;top:3788px" aria-label="Social media links"><span></span><span></span><span></span></div>

  <h4 class="abs display footer-title" style="left:864px">Newsletter</h4>
  <p class="abs" style="left:864px;top:3714px;width:250px;font-size:16px;line-height:25px;color:var(--footer-text)">Be the first who learns about our great promotions!</p>
  <div class="abs newsletter-input"><span class="field">Enter you email...</span><span class="go">SUBSCRIBE</span></div>

  <div class="abs footer-rule"></div>
  <p class="abs copyright">Copyright Timberpour.2023 All Rights Reserved</p>
</footer>

</body>
</html>
```